Gutschein-Design für Lorenzo Restaurant
Zielgruppe
Pizzeria Restaurant à la carte/ Das Design soll Jedem gefallen, mir, Familien, Pärchen, etc.
Aufgabenstellung
Die Gutscheine werden von unserem Kassensystem bedruckt. Die Größe ist ca. 95 mm/ 80 mm. Dieser Bon sollte in die Gutschein-Hülle, die ich jetzt brauche eingesteckt sein. Die Masse sollen 105x105 mm sein, offen 105x210 mm .
Text:
Auf Seite 1:
- Das Logo
- Geschenk-Gutschein
Auf Seite 2:
- Der Gutschein kann für Vieles gut sein
- In unserem Fall lässt unsere reichhaltige Karte viele Möglichkeiten offen
- Auf jeden Fall wird bestimmt geschlemmt, geschmaust und genossen
- Wir wünschen guten Appetit
Auf Seite 3 für die Druckerei:
- 2 Halbkreise gestanzt und 1x gerillt, rundum auf Endformat beschnitten.
- 1-Bruch Falz
Hier gehört der Gutschein-Bon 95/80 mm eingesteckt
Auf Seite 4:
Lorenzo
Restaurantbetriebsgesellschaft m.b.H.
www.lorenzo-trattoria.at
Im Dateiupload habe ich als ein Beispiel die jetzigen Gutscheinhuelle beigefügt.
MfG

```html
<!DOCTYPE html>
<html lang="de">
<head>
<meta charset="utf-8">
<title>Lorenzo – Gutschein-Hülle</title>
<link rel="stylesheet" href="https://fonts.googleapis.com/css2?family=Barlow+Semi+Condensed:wght@400;500;600&family=Saira+Extra+Condensed:wght@500;600&display=swap">
<style>
  :root {
    --wine: #6e0c0f;
    --wine-text: #7a0f1a;
    --cream: #f1df9a;
    --paper: #f9fafc;
    --gap: #ffffff;
    --dash: #f4ecd8;
    --art-wine: #c9a2a2;
    --art-cream: #d9c27c;
  }
  html, body { margin: 0; padding: 0; overflow: hidden; background: var(--gap); }
  .canvas { position: relative; width: 999px; height: 1200px; overflow: hidden; background: var(--gap); }

  .panel { position: absolute; left: 0; width: 999px; overflow: hidden; }
  .panel--outer { top: 0; height: 573px; }
  .panel--inner { top: 629px; height: 571px; }
  .panel__bg, .panel__type { position: absolute; inset: 0; width: 100%; height: 100%; display: block; }
  .panel__type { pointer-events: none; }

  .display { font-family: "Saira Extra Condensed", "Arial Narrow", sans-serif; font-weight: 600; }
  .display--wine { fill: var(--wine-text); }
  .display--white { fill: #ffffff; }
  .body-text { font-family: "Barlow Semi Condensed", "Arial Narrow", sans-serif; }

  .company { position: absolute; left: 42px; top: 240px; margin: 0; font-style: normal; color: var(--wine-text); font-size: 16px; line-height: 21px; font-weight: 500; }
  .company p { margin: 0 0 10px; }
  .company__name { font-weight: 600; font-size: 21px; line-height: 24px; margin-bottom: 2px !important; }
  .company__legal { font-weight: 600; }

  .message { position: absolute; left: 150px; top: 24px; color: var(--wine-text); font-size: 22.5px; line-height: 31px; font-weight: 500; }
  .message p { margin: 0 0 12px; }

  .art { position: absolute; border-radius: 50%; }
  .art--pizza { left: 394px; top: 0; width: 235px; height: 291px; border-radius: 0 0 50% 40%; background: radial-gradient(circle at 40% 40%, #e7d2d2, var(--art-wine)); opacity: .55; }
  .art--tomato-slice { left: 37px; top: 426px; width: 89px; height: 63px; background: var(--art-wine); opacity: .5; }
  .art--basil { left: 357px; top: 434px; width: 74px; height: 80px; background: var(--art-wine); opacity: .5; }
  .art--tomato { left: 909px; top: 491px; width: 63px; height: 63px; background: var(--art-wine); opacity: .5; }
  .art--mushroom { left: 857px; top: 40px; width: 94px; height: 83px; background: var(--art-cream); opacity: .45; }
  .art--onions { left: 463px; top: 272px; width: 177px; height: 146px; background: var(--art-cream); opacity: .35; }
</style>
</head>
<body>
<div class="canvas">

  <section class="panel panel--outer">
    <svg class="panel__bg" viewBox="0 0 1748 1002" preserveAspectRatio="none" aria-hidden="true">
      <defs>
        <filter id="soft-shadow" x="-10%" y="-10%" width="120%" height="130%">
          <feDropShadow dx="0" dy="14" stdDeviation="12" flood-color="#3a0407" flood-opacity=".45"/>
        </filter>
      </defs>
      <rect width="1748" height="1002" fill="var(--wine)"/>
      <path d="M0,305 C300,270 500,320 650,520 C800,720 1000,920 1300,935 C1500,940 1650,870 1748,790 L1748,1002 L0,1002 Z" fill="var(--cream)"/>
      <path d="M0,305 C300,270 500,320 650,520 C800,720 1000,920 1300,935 C1500,940 1650,870 1748,790 L1748,0 L0,0 Z" fill="var(--wine)" filter="url(#soft-shadow)"/>
      <circle cx="1330" cy="200" r="645" fill="var(--paper)" filter="url(#soft-shadow)"/>
      <path d="M345,140 A105,105 0 0 0 555,140" fill="none" stroke="var(--dash)" stroke-width="5" stroke-dasharray="14 12"/>
      <path d="M345,840 A105,105 0 0 1 555,840" fill="none" stroke="var(--paper)" stroke-width="5" stroke-dasharray="14 12"/>
    </svg>

    <div class="art art--pizza" role="img" aria-label="Linienzeichnung einer Pizza mit Pilzen und Oliven"></div>
    <div class="art art--tomato-slice" role="img" aria-label="Gezeichnete Tomatenscheibe"></div>
    <div class="art art--basil" role="img" aria-label="Gezeichnete Basilikumblätter"></div>
    <div class="art art--tomato" role="img" aria-label="Gezeichnete Tomate"></div>

    <svg class="panel__type" viewBox="0 0 999 573">
      <text class="display display--wine wordmark" x="766" y="91" font-size="64" textLength="132" lengthAdjust="spacingAndGlyphs">lorenzo</text>
      <text class="display display--wine title" x="612" y="283" font-size="118" textLength="279" lengthAdjust="spacingAndGlyphs">gutschein</text>
      <text class="display display--wine tagline" x="628" y="428" font-size="30" textLength="258" lengthAdjust="spacingAndGlyphs" transform="rotate(3 628 428)">das original. schmeckt besser.</text>
      <text class="display display--wine website" x="140" y="522" font-size="31" textLength="220" lengthAdjust="spacingAndGlyphs">www.lorenzo-trattoria.at</text>
    </svg>

    <address class="company body-text">
      <p class="company__name">Lorenzo</p>
      <p class="company__legal">Restaurantbetriebsgesellschaft m.b.H.</p>
      <p>Lindengasse 12<br>3270 Scheibbs</p>
      <p>Telefon: +43 (7482) 418 90<br>info@lorenzo-trattoria.at</p>
    </address>
  </section>

  <section class="panel panel--inner">
    <svg class="panel__bg" viewBox="0 0 1748 1000" preserveAspectRatio="none" aria-hidden="true">
      <defs>
        <filter id="soft-shadow-2" x="-10%" y="-10%" width="120%" height="130%">
          <feDropShadow dx="0" dy="14" stdDeviation="12" flood-color="#3a0407" flood-opacity=".45"/>
        </filter>
      </defs>
      <rect width="1748" height="1000" fill="var(--wine)"/>
      <path d="M0,500 C300,590 550,600 800,680 C1000,750 1200,860 1350,860 C1500,860 1650,790 1748,735 L1748,1000 L0,1000 Z" fill="var(--cream)"/>
      <path d="M0,1000 C150,810 380,700 620,700 C900,700 1080,850 1330,852 C1530,854 1670,800 1748,760 L1748,1000 Z" fill="var(--wine)" filter="url(#soft-shadow-2)"/>
      <path d="M700,1000 C1000,975 1320,965 1748,880 L1748,1000 Z" fill="var(--cream)"/>
      <path d="M900,1000 C1200,985 1500,975 1748,940 L1748,1000 Z" fill="var(--wine)"/>
      <circle cx="430" cy="-71" r="646" fill="var(--paper)" filter="url(#soft-shadow-2)"/>
      <path d="M1192,155 A108,108 0 0 0 1408,155" fill="none" stroke="var(--dash)" stroke-width="5" stroke-dasharray="14 12"/>
      <path d="M1192,850 A108,108 0 0 1 1408,850" fill="none" stroke="var(--paper)" stroke-width="5" stroke-dasharray="14 12"/>
    </svg>

    <div class="art art--mushroom" role="img" aria-label="Gezeichneter Champignon"></div>
    <div class="art art--onions" role="img" aria-label="Zwei gezeichnete Zwiebeln"></div>

    <div class="message body-text">
      <p>Ein Gutschein<br>kann für Vieles gut sein.</p>
      <p>In unserem Fall lässt<br>unsere reichhaltige Karte<br>viele Möglichkeiten offen.</p>
      <p>Auf jeden Fall wird bestimmt<br>geschlemmt, geschmaust<br>und genossen.</p>
    </div>

    <svg class="panel__type" viewBox="0 0 999 571">
      <text class="display display--white wish" x="180" y="471" font-size="31" textLength="238" lengthAdjust="spacingAndGlyphs">wir wünschen guten appetit.</text>
    </svg>
  </section>

</div>
</body>
</html>
```